Social Business Consultancy

Kavora Ventures is a start up consultancy but with a difference: were non-corporate. We work in the field of economic development in low income countries and we focus on entrepreneurship but with a social and or environmental mission.

The type of projects we work on are innovative, ground breaking, different, edgy and bold. We are young, determined, , unreasonnable and undeterred by challenges.
We want our website to convey these ideas.
Updates

Hello,

Could you please include the option of having the website in two languages. Thank you.

Please note that new files have been added to the project brief.

- FrontPage  Main Photo (Grey dirt Road)
- WordCloud Photo to be used on the home page (as a small image )

The website should keep these colour tones.

Thank you !

Hello,

Wireframes have been uploaded. Please use as an indication.

Thanks,
n.

Target Market(s)

Governments, development agencies, social investors, NGOs, banks and social entrepreneurs.

Industry/Entity Type

Consulting

Requirements
Must have
• We already have a logo and business cards (provided). We want the website to look professional, yet simple with a maximum of two or three colours. We want the look to be seamless. There is no need for too many boxes or categories.
Nice to have
• We want bold, edgy, modern  and professional look .
• Examples:
• http://www.brightmarrowlab.org/
• http://www.pavelstone.com/
• http://www.tarnhiring.co.nz/
Should not have
• The design should not use old style fonts.

```html
<!DOCTYPE html>
<html lang="en">
<head>
<meta charset="utf-8">
<title>Kavora Ventures – Social Business Consultancy</title>
<link rel="stylesheet" href="https://fonts.googleapis.com/css2?family=Yanone+Kaffeesatz:wght@300;400&family=Arimo:wght@400;700&family=Open+Sans:wght@400;600&display=swap">
<style>
  :root{
    --sky:#08a6ec;
    --sky-light:#bfe8fb;
    --navy:#1d2b44;
    --green:#96d03a;
    --green-dark:#7ab52a;
    --page:#e8e6e6;
    --frame:#666666;
    --text:#222222;
    --orange:#f2690f;
    --footer:#231f20;
    --footer-blue:#1ea5e2;
    --lime:#c9de2c;
    --red-orange:#f15a24;
    --yellow:#f6e500;
    --white:#ffffff;
  }
  *{margin:0;padding:0;box-sizing:border-box}
  html,body{width:1200px;height:987px;overflow:hidden;background:var(--page)}
  body{position:relative;font-family:"Open Sans",sans-serif;color:var(--text)}

  .site-header{position:absolute;left:0;top:0;width:1200px;height:188px;
    background:linear-gradient(to bottom,#ffffff 0%,var(--sky-light) 35%,var(--sky) 100%)}
  .brand-name{position:absolute;left:64px;top:70px;font-family:"Arimo",sans-serif;font-weight:400;
    font-size:46px;line-height:1;color:var(--navy)}
  .brand-tagline{position:absolute;left:66px;top:134px;font-family:"Arimo",sans-serif;font-size:15px;color:var(--navy)}
  .call-us{position:absolute;right:56px;top:66px;text-align:right;font-family:"Yanone Kaffeesatz",sans-serif;line-height:1.05}
  .call-us .lead{font-size:35px;color:var(--navy)}
  .call-us .phone{font-size:33px;color:var(--white)}

  .main-nav{position:absolute;left:0;top:188px;width:1200px;height:50px;
    background:linear-gradient(to bottom,#aee05a 0%,var(--green) 50%,var(--green-dark) 100%);
    border-top:1px solid #6fa51f;border-bottom:1px solid #6fa51f;
    display:flex;align-items:center;justify-content:center;
    font-family:"Yanone Kaffeesatz",sans-serif;font-size:28px;color:#2b2b2b}
  .main-nav span{padding:0 34px}
  .main-nav .sep{padding:0;font-size:26px}

  .feature{position:absolute;top:261px;width:352px;height:197px;background:var(--frame);padding:10px}
  .feature .visual{position:relative;width:100%;height:100%;overflow:hidden}
  .feature .caption{position:absolute;left:0;bottom:0;width:100%;height:40px;background:rgba(40,40,40,.72);
    color:var(--white);font-family:"Arimo",sans-serif;font-size:26px;text-align:center;line-height:40px}
  .f1{left:60px}.f2{left:426px}.f3{left:793px}
  .f1 .visual{background:radial-gradient(circle at 50% 40%,#e24fd0 0%,#3a7ad8 30%,#0a1a2c 65%,#000 100%)}
  .f2 .visual{background:linear-gradient(90deg,#3a88c2 0%,#c84a2c 30%,#e0a050 55%,#f6f6f4 75%,#ffffff 100%)}
  .f3 .visual{background:linear-gradient(100deg,#7ab6d8 0%,#b8d6a0 45%,#d9a078 75%,#9c6a44 100%)}

  .block{position:absolute;width:532px}
  .block.left{left:57px}
  .block.right{left:635px;width:507px}
  .block h2{font-family:"Arimo",sans-serif;font-weight:700;color:#222;font-size:17px;line-height:28px;
    padding-bottom:6px;border-bottom:2px dotted #555;white-space:nowrap}
  .block h2 .accent{color:var(--orange);font-size:24px;font-weight:700;margin-left:6px}
  .block h2 .accent.big{font-size:29px}
  .block p{font-size:12px;line-height:21.6px;margin-top:12px;padding-left:1px}
  .read-more{position:absolute;width:101px;height:26px;border:1px solid #4b8fb0;
    background:linear-gradient(to bottom,#c9ecfb 0%,#6cc8f0 50%,#2fa8e0 100%);
    font-family:"Arimo",sans-serif;font-weight:700;font-size:13px;color:#0f1f2a;text-align:center;line-height:24px}

  .site-footer{position:absolute;left:0;top:845px;width:1200px;height:142px;background:var(--footer);color:var(--white)}
  .footer-brand{position:absolute;left:59px;top:16px;font-family:"Arimo",sans-serif;font-weight:700;font-size:25px;color:var(--footer-blue)}
  .footer-address{position:absolute;left:58px;top:50px;font-family:"Arimo",sans-serif;font-size:14px;line-height:17.5px;color:var(--lime)}
  .footer-divider{position:absolute;left:260px;top:47px;height:72px;border-left:2px dotted #777}
  .footer-contact{position:absolute;left:278px;top:51px;font-family:"Arimo",sans-serif;font-weight:700;font-size:13.5px;line-height:17.5px}
  .footer-contact .label{color:var(--red-orange)}
  .footer-contact .yellow{color:var(--yellow)}
  .footer-links{position:absolute;right:58px;top:52px;font-family:"Arimo",sans-serif;font-size:13px;text-align:right;white-space:nowrap}
  .footer-links span.sep{margin:0 9px}
  .copyright{position:absolute;right:58px;top:76px;font-family:"Arimo",sans-serif;font-size:12.5px}
</style>
</head>
<body>
  <header class="site-header">
    <div class="brand-name">Kavora Ventures</div>
    <div class="brand-tagline">Social Business Consultancy</div>
    <div class="call-us">
      <div class="lead">FEEL FREE TO CALL US</div>
      <div class="phone">Tel : +33(0)6 41 27 58 03</div>
    </div>
  </header>

  <nav class="main-nav">
    <span>Home</span><span class="sep">|</span>
    <span>About Us</span><span class="sep">|</span>
    <span>Our Mission</span><span class="sep">|</span>
    <span>Services</span><span class="sep">|</span>
    <span>Solutions</span><span class="sep">|</span>
    <span>Clients</span><span class="sep">|</span>
    <span>Blogs</span><span class="sep">|</span>
    <span>Contact Us</span>
  </nav>

  <div class="feature f1"><div class="visual" role="img" aria-label="Glowing multicoloured brain inside a human head silhouette on black"><div class="caption">Innovative Thinking</div></div></div>
  <div class="feature f2"><div class="visual" role="img" aria-label="Row of coloured pencils decreasing in height on white"><div class="caption">Reducing Proverty</div></div></div>
  <div class="feature f3"><div class="visual" role="img" aria-label="Smiling curly-haired child outdoors under a blue sky"><div class="caption">Changing Lives</div></div></div>

  <section class="block left" style="top:478px">
    <h2>Welcome to<span class="accent">KAVORA</span></h2>
    <p>Lorem ipsum dolor sit amet, consectetur adipiscing elit. Maecenas luctus arcu sit amet quam viverra condimentum. Suspendisse aliquam ullamcorper sapien suscipit laoreet. Suspendisse varius sodales lectus sit amet convallis. Vestibulum facilisis condimentum lorem, quis commodo tortor luctus eget.</p>
  </section>
  <div class="read-more" style="left:56px;top:623px">read more</div>

  <section class="block right" style="top:478px">
    <h2>our<span class="accent">SERVICES</span></h2>
    <p>We offer technical assistance (design, implement and monitor) for projects that serve a social and / or environmental purpose while maintaining have a profit generating ethos. We thrive for a triple bottom line approach of balancing commercial, social and environmental objectives. This is a key component of our work.</p>
  </section>
  <div class="read-more" style="left:637px;top:623px">read more</div>

  <section class="block left" style="top:664px">
    <h2>our<span class="accent big">MISSION</span></h2>
    <p>To contribute to poverty reduction by channeling human and investment capital in projects that offer increased access to socially and environmentally beneficial products and services for the Bottom of the Pyramid ("BOP").</p>
  </section>
  <div class="read-more" style="left:56px;top:796px">read more</div>

  <section class="block right" style="top:664px">
    <h2>our<span class="accent">CLIENTS</span></h2>
    <p>We are a &nbsp;small consultancy that works with governments, investment managers, development organisations, banks and private investors to help develop social businesses in developping countries.</p>
  </section>
  <div class="read-more" style="left:636px;top:796px">read more</div>

  <footer class="site-footer">
    <div class="footer-brand">KAVORA</div>
    <div class="footer-address">“le héron”<br>24 Rue des Lilas<br>06000 NICE</div>
    <div class="footer-divider"></div>
    <div class="footer-contact">
      <div><span class="label">Tel :</span> <span class="yellow">+33(0)6 41 27 58 03</span></div>
      <div><span class="label">Email :</span> maren.lidell@kavoraventures.com</div>
      <div><span class="label">Skype :</span> maren.lidell</div>
    </div>
    <div class="footer-links">Home<span class="sep">|</span>About Us<span class="sep">|</span>Our Mission<span class="sep">|</span>Services<span class="sep">|</span>Solutions<span class="sep">|</span>Clients<span class="sep">|</span>Blogs<span class="sep">|</span>Contact Us</div>
    <div class="copyright">© 2010 Kavoraventures.com | All rights reserved</div>
  </footer>
</body>
</html>
```